Dog care service needs business card design

Our company is Paws Harbour. We provide care for dogs while their owners are away, either through home visits or a holiday stay in the homes of carefully selected minders. Our existing website & Chatterbook cover should provide all the colour cues for our business cards - namely blues, blondes and grey. We have an existing logo (provided).

www.pawsharbourcare.example.au
www.facebook.com/pawsharbourcareau

We wish to clearly communicate our three areas of service "dog minding, home visits, dog walking".

We would like to have the files ready for upload to Printlyne (or similar) for immediate printing.

Target Market(s)

Dog owners who love their dogs like family

Industry/Entity Type

Business

Contact Information for Business Card

Paws Harbour
Ph: 0417 358 904

Font styles to use
Sans Serif

Colors
33a6d7
3176b5

Requirements
Must have
• Logo
• Telephone number
• website
• "Dog minding, home visits, dog walking"
Should not have
• any additional illustrations beyond the logo.

```html
<!DOCTYPE html>
<html lang="en">
<head>
<meta charset="utf-8">
<title>Paws Harbour – Business Card</title>
<link rel="stylesheet" href="https://fonts.googleapis.com/css2?family=Open+Sans:wght@400;600;700;800&display=swap">
<style>
  :root {
    --page: #ffffff;
    --card-edge: #9fbad6;
    --card-mid: #c3d6ea;
    --card-light: #eef4fa;
    --card-flat: #b3cbe3;
    --navy: #2c3a54;
    --blue: #33a6d7;
    --blue-deep: #3176b5;
    --strip: #9bb6d3;
  }
  * { margin: 0; padding: 0; box-sizing: border-box; }
  html, body {
    width: 1200px;
    height: 3896px;
    overflow: hidden;
    background: var(--page);
    font-family: "Open Sans", Arial, sans-serif;
    color: var(--navy);
  }
  .sheet { position: relative; width: 1200px; height: 3896px; }

  .card {
    position: absolute;
    left: 272px;
    width: 760px;
    overflow: hidden;
  }

  /* Front */
  .card--front {
    top: 0;
    height: 1320px;
    background: radial-gradient(ellipse 70% 45% at 50% 50%, var(--card-light) 0%, var(--card-mid) 55%, var(--card-edge) 100%);
  }
  .brand {
    position: absolute;
    display: flex;
    align-items: center;
  }
  .brand__mark {
    border-radius: 50%;
    background: var(--navy);
    flex: none;
  }
  .brand__name {
    font-weight: 700;
    color: var(--navy);
    line-height: 0.95;
    letter-spacing: -1px;
  }
  .card--front .brand { left: 40px; top: 560px; gap: 34px; }
  .card--front .brand__mark { width: 170px; height: 170px; }
  .card--front .brand__name { font-size: 104px; }

  /* Back */
  .card--back {
    top: 1340px;
    height: 1332px;
    background: var(--card-flat);
  }
  .pattern-strip {
    position: absolute;
    left: 0;
    top: 20px;
    width: 760px;
    height: 100px;
    background: linear-gradient(90deg, var(--strip), #a9c1db, var(--strip));
  }
  .card--back .brand { left: 30px; top: 770px; gap: 18px; }
  .card--back .brand__mark { width: 92px; height: 92px; }
  .card--back .brand__name { font-size: 54px; }

  .services {
    position: absolute;
    left: 30px;
    top: 900px;
    list-style: none;
  }
  .services__item {
    display: flex;
    align-items: center;
    gap: 18px;
    height: 52px;
    font-size: 34px;
    color: var(--navy);
  }
  .services__icon { width: 36px; height: 30px; flex: none; }

  .contact {
    position: absolute;
    left: 0;
    width: 760px;
    top: 1190px;
    text-align: center;
    color: var(--navy);
  }
  .contact__phone { font-size: 34px; line-height: 60px; }
  .contact__web { font-size: 34px; font-weight: 600; line-height: 60px; }
</style>
</head>
<body>
<main class="sheet">

  <section class="card card--front" aria-label="Card front">
    <div class="brand">
      <span class="brand__mark"></span>
      <span class="brand__name">Paws<br>Harbour</span>
    </div>
  </section>

  <section class="card card--back" aria-label="Card back">
    <div class="pattern-strip" role="img" aria-label="Row of repeated small brand marks along the top edge"></div>

    <div class="brand">
      <span class="brand__mark"></span>
      <span class="brand__name">Paws<br>Harbour</span>
    </div>

    <ul class="services">
      <li class="services__item">
        <svg class="services__icon" viewBox="0 0 36 30" aria-hidden="true">
          <g fill="var(--navy)">
            <circle cx="6" cy="11" r="5"/><circle cx="6" cy="19" r="5"/>
            <circle cx="30" cy="11" r="5"/><circle cx="30" cy="19" r="5"/>
            <rect x="6" y="11" width="24" height="8"/>
          </g>
        </svg>
        Dog minding
      </li>
      <li class="services__item">
        <svg class="services__icon" viewBox="0 0 36 30" aria-hidden="true">
          <path d="M3 10 H33 L29 26 H7 Z" fill="var(--navy)"/>
        </svg>
        Home visits
      </li>
      <li class="services__item">
        <svg class="services__icon" viewBox="0 0 36 30" aria-hidden="true">
          <g fill="var(--navy)">
            <ellipse cx="18" cy="21" rx="8" ry="7"/>
            <circle cx="9" cy="12" r="3.5"/><circle cx="15" cy="6" r="3.5"/>
            <circle cx="21" cy="6" r="3.5"/><circle cx="27" cy="12" r="3.5"/>
          </g>
        </svg>
        Dog walking
      </li>
    </ul>

    <div class="contact">
      <p class="contact__phone">tel: 0417 358 904</p>
      <p class="contact__web">www.pawsharbourcare.example.au</p>
    </div>
  </section>

</main>
</body>
</html>
```